MODELS AGENCY NEW YEAR 2026 CARD

A 10 cm x 21 cm horizontal New Year card for clients of our 2 models agencies, Pommelin (kids) and Velvaride (actors and adults) (logo in the jobs).

Side A of the card: creative mission:
-text: 2026
-text: Peace and Love
-Studio or movie set atmosphere
-tone of voice: optimistic, positive, colorful

Side B:
(name of 4 people of the agency:)
Odette, Anne-Sophie, Hortense & Luc-Antoine,
(2 logos)
Pommelin & VelvaRide
(Adres)
Rue des Tilleuls 74 b3 - 1200 Bruxelles - Belgique

Target Market(s)

Movie directors, photographers

Industry/Entity Type

Fashion, advertising & Movies

Requirements
Must have
• SEE TEXT IN BRIEFING

```html
<!DOCTYPE html>
<html lang="en">
<head>
<meta charset="utf-8">
<title>Pommelin &amp; Velvaride – New Year Card 2026</title>
<link href="https://fonts.googleapis.com/css2?family=Russo+One&family=Roboto:wght@400;500&display=swap" rel="stylesheet">
<style>
  :root {
    --page-grey: #b3b3b3;
    --navy: #02506e;
    --blue: #006791;
    --sky: #0a9ade;
    --white: #ffffff;
    --ink: #0a0a0a;
    --purple: #4a2a6b;
    --muted: #7a6a86;
    --frame: #dcdcdc;
  }
  * { margin: 0; padding: 0; box-sizing: border-box; }
  html, body { width: 1200px; height: 1200px; overflow: hidden; background: var(--page-grey); }
  .canvas { position: relative; width: 1200px; height: 1200px; font-family: "Russo One", sans-serif; }
  .side { position: absolute; top: 131px; width: 446px; height: 935px; overflow: hidden; }
  .side-a { left: 148px; background: var(--navy); }
  .side-b { left: 617px; background: var(--white); }
  .side svg.scene { position: absolute; left: 0; top: 0; width: 446px; height: 935px; }

  .year-box {
    position: absolute; left: 46px; top: 60px; width: 343px; height: 134px;
    background: var(--blue); color: var(--white);
    display: flex; align-items: center; justify-content: center;
    font-size: 104px; line-height: 1; letter-spacing: 1px;
  }
  .headline { position: absolute; left: 56px; top: 230px; color: var(--white); line-height: 1; }
  .headline .big { display: block; font-size: 104px; }
  .headline .small { display: block; font-size: 70px; margin-top: 10px; }

  .agency-tag {
    position: absolute; left: 112px; top: 34px; width: 222px; height: 66px;
    background: var(--blue); color: var(--white);
    display: flex; align-items: center; justify-content: center;
    font-size: 50px; line-height: 1;
  }
  .team { position: absolute; left: 73px; top: 128px; list-style: none; color: var(--ink); font-size: 31px; line-height: 46px; }

  .brand-card {
    position: absolute; top: 339px; width: 180px; height: 119px;
    background: var(--white); border: 2px solid var(--frame);
    box-shadow: 0 1px 3px rgba(0,0,0,.15);
    display: flex; flex-direction: column; align-items: center; justify-content: center;
    text-align: center;
  }
  .brand-card.velvaride { left: 27px; }
  .brand-card.pommelin { left: 231px; }
  .brand-name { font-size: 24px; color: var(--purple); line-height: 1; }
  .brand-line { font-family: "Roboto", sans-serif; font-size: 7.5px; letter-spacing: 1px; color: var(--purple); margin-top: 6px; }
  .brand-since { font-family: "Roboto", sans-serif; font-size: 5.5px; color: var(--muted); margin-top: 16px; }

  .address {
    position: absolute; left: 0; bottom: 0; width: 446px; height: 44px;
    background: var(--blue); color: var(--white);
    display: flex; align-items: center; padding-left: 14px; gap: 10px;
    font-size: 13.4px; letter-spacing: .2px;
  }
  .address svg { width: 14px; height: 18px; flex: none; }
</style>
</head>
<body>
<div class="canvas">

  <section class="side side-a">
    <svg class="scene" viewBox="0 0 446 935">
      <defs>
        <linearGradient id="studioTone" x1="0" y1="0" x2="0" y2="1">
          <stop offset="0" stop-color="#3a3c40"/>
          <stop offset=".35" stop-color="#c9ccce"/>
          <stop offset=".65" stop-color="#8a8c8e"/>
          <stop offset="1" stop-color="#2c2d30"/>
        </linearGradient>
      </defs>
      <rect x="0" y="430" width="446" height="505" fill="url(#studioTone)" role="img" aria-label="Photo of a film studio set with crew, lights and cameras"/>
      <path d="M0 434 C90 420 180 450 260 500 C330 545 400 560 446 456 L446 0 L0 0 Z" fill="var(--sky)"/>
      <path d="M0 447 C90 432 180 470 260 520 C330 565 400 580 446 480 L446 0 L0 0 Z" fill="var(--blue)"/>
      <path d="M0 457 C100 440 190 480 270 520 C340 550 410 555 446 456 L446 0 L0 0 Z" fill="var(--navy)"/>
    </svg>
    <div class="year-box">2026</div>
    <h1 class="headline"><span class="big">PEACE</span><span class="small">AND LOVE</span></h1>
  </section>

  <section class="side side-b">
    <svg class="scene" viewBox="0 0 446 935">
      <defs>
        <linearGradient id="setTone" x1="0" y1="0" x2="1" y2="1">
          <stop offset="0" stop-color="#9fb3c6"/>
          <stop offset=".5" stop-color="#e2d6c2"/>
          <stop offset="1" stop-color="#b49a78"/>
        </linearGradient>
      </defs>
      <rect x="0" y="480" width="446" height="455" fill="url(#setTone)" role="img" aria-label="Photo of a period movie set with actors seated in director chairs and a camera"/>
      <path d="M0 488 C90 460 200 500 290 550 C350 585 400 600 446 514 L446 0 L0 0 Z" fill="var(--sky)"/>
      <path d="M0 508 C100 480 210 540 300 585 C360 610 410 600 446 514 Z" fill="var(--blue)"/>
      <path d="M0 508 C100 480 200 525 290 570 C330 585 360 585 380 580 C300 560 200 495 0 503 Z" fill="var(--sky)"/>
      <path d="M0 507 C100 475 200 520 290 565 C340 585 360 585 370 582 C420 560 440 530 446 514 L446 0 L0 0 Z" fill="var(--white)"/>
    </svg>

    <div class="agency-tag">AGENCY</div>
    <ol class="team">
      <li>1.ODETTE</li>
      <li>2.ANNE-SOPHIE</li>
      <li>3.HORTENSE</li>
      <li>4.LUC-ANTOINE</li>
    </ol>

    <div class="brand-card velvaride">
      <div class="brand-name">VELVARIDE</div>
      <div class="brand-line">PEOPLE, ACTORS &amp; MODELS AGENCY</div>
      <div class="brand-since">– SINCE 2000 –</div>
    </div>
    <div class="brand-card pommelin">
      <div class="brand-name">POMMELIN</div>
      <div class="brand-line">CHILDREN MODELS AGENCY</div>
      <div class="brand-since">– SINCE 1982 –</div>
    </div>

    <div class="address">
      <svg viewBox="0 0 14 18" aria-hidden="true"><path d="M7 0C3.1 0 0 3.1 0 7c0 5 7 11 7 11s7-6 7-11C14 3.1 10.9 0 7 0z" fill="#fff"/><circle cx="7" cy="7" r="2.6" fill="#006791"/></svg>
      <span>RUE DES TILLEULS 74 B3 - 1200 BRUXELLES - BELGIQUE</span>
    </div>
  </section>

</div>
</body>
</html>
```